Custom Proposal

We need a custom proposal template created for our company. Our company, BRIGHTWAVE AUDIO SERVICES, provides in-store music and messaging services to businesses in the US and Canada. We need a 3-4 page document created that outlines our products and services that will accompany their proposal. The proposal needs to be created using company colors with a fresh feeling. Our music service is top quality and we service many major brands with customized music service. We have all of the copy and logos for partner companies. We need a designer to create a layout that will express our products and services in a fresh and exciting way.

Attached to this project you will find the following:

- PDF file title "Example". This is an example file of what we are looking for (minus the last page with the order fields).

- BRIGHTWAVE AUDIO SERVICES logo in EPS

- BRIGHTWAVE AUDIO SERVICES brand standards guideline

- Text copy for the flyer

- Styles (these match our web site)

- Font used on our web site and other material

- Zip file with logos of companies we do business with

We would also like a section that has the logos for these companies to showcase who we work with.

We prefer to have the project developed in an editable format such as Adobe Illustrator or PSD.

The paper size is 8 1/2" x 11" Portrait
Updates

Please note: We do NOT want the graphics included in the "Brands Standard Guide" that is attached to the project to be used for the project. The Brand Standards Guide is provided simply to show you how to use our logo, not to include the graphics used in the guide. Also, we do not want any computers or smart phones in the artwork. We provided the Pelican Harbor document as an example of one we liked, not to use the same graphics.

Please be sure to follow the outline of the project and use the images  supplied. Please also keep in mind we  are not looking for a template look  but rather  a  unique design  for each page that is themed for our industry. Our industry is in-store music and messaging services.

Thank you

Target Market(s)

Business owners, executives, marketing directors, business executives

Industry/Entity Type

Business

Requirements
Must have
• We are looking for fresh, open, personal, exciting, creative, and relevant designs.
Should not have
• We are NOT looking for stock template looking designs with no originality that look like a standard stock design.

```html
<!DOCTYPE html>
<html lang="en">
<head>
<meta charset="utf-8">
<title>BrightWave Audio Services – Proposal Pages 3 &amp; 4</title>
<link href="https://fonts.googleapis.com/css2?family=Questrial&family=Lato:ital,wght@0,300;0,400;0,700;1,300&family=Open+Sans:ital,wght@1,800&display=swap" rel="stylesheet">
<style>
:root{
  --green:#b9cd2d;
  --ink:#4a4a4a;
  --body:#555555;
  --muted:#8a8a8a;
  --footer:#58595b;
  --paper:#ffffff;
  --stage:#ece8e2;
  --line:#d6d6d6;
}
*{box-sizing:border-box;margin:0;padding:0}
html,body{width:1200px;height:867px;overflow:hidden}
body{background:var(--stage);font-family:"Lato",sans-serif;color:var(--ink);position:relative}
.page-label{position:absolute;top:38px;font:italic 800 22px "Open Sans",sans-serif;color:#fff;text-shadow:0 1px 2px rgba(0,0,0,.35)}
.page{position:absolute;top:88px;width:550px;height:710px;background:var(--paper);box-shadow:0 4px 10px rgba(0,0,0,.25);overflow:hidden}
.page--products{left:22px}
.page--advantage{left:625px}
.masthead{position:absolute;left:0;top:0;width:550px;height:62px}
.masthead svg{display:block}
.masthead__art{position:absolute;left:0;top:0;width:180px;height:44px;background:linear-gradient(90deg,#5d5d5d,#9a9a9a 45%,rgba(185,205,45,0))}
.brand{position:absolute;right:38px;top:16px;display:flex;align-items:center;gap:8px;color:#fff}
.brand__mark{width:22px;height:22px;border:2px solid #fff}
.brand__name{font:400 13px/1.05 "Questrial",sans-serif;border-left:1px solid #fff;padding-left:8px}
.footer{position:absolute;left:0;bottom:0;width:550px;height:70px;z-index:1}
.footer svg{position:absolute;left:0;top:0}
.footer__call{position:absolute;left:50px;top:14px;font:700 15px/1.3 "Lato",sans-serif;color:#fff}
.footer__call span{display:block;color:var(--green)}
.footer__web{position:absolute;right:40px;top:36px;font:700 13.5px "Lato",sans-serif;color:#fff;letter-spacing:.2px}
h1,h2,h3{font-weight:400}
.title{position:absolute;left:50px;top:70px;font:400 27px "Questrial",sans-serif;color:var(--green);white-space:nowrap}
.title small{font-size:14px;color:var(--muted);margin-left:10px}
.block{position:absolute}
.section-head{font:400 18px/1.1 "Questrial",sans-serif;color:var(--green);white-space:nowrap}
.kicker{font:400 9.5px/1.25 "Lato",sans-serif;text-transform:uppercase;color:#333;margin-top:4px}
.minor-head{font:400 9.5px "Lato",sans-serif;text-transform:uppercase;color:#333}
.minor-head--muted{color:var(--muted)}
p{font-size:7.8px;line-height:10.6px;color:var(--body);margin-top:2px;text-align:justify}
p + p{margin-top:6px}
.lead{font-weight:700;color:#444}
.bullets{list-style:none;margin-top:6px}
.bullets li{font-size:7.8px;color:var(--body);padding-left:10px;position:relative;line-height:16px}
.bullets li::before{content:"";position:absolute;left:0;top:5px;width:5px;height:5px;background:var(--green)}
.bullets--caps li{text-transform:uppercase;line-height:10.5px;margin-bottom:5.5px}
.bullets--caps li::before{top:2.5px}
.illustration{position:absolute;background:linear-gradient(180deg,#e9a44a 0%,#6c8fb8 35%,#2c2a28 62%,#d9d9d9 100%);border-radius:6px;z-index:2}
.puzzle{position:absolute;background:linear-gradient(135deg,#c8d94a,#8fa020);border-radius:3px}
.quote{font:italic 300 16px/1.3 "Lato",sans-serif;color:#9a9a9a}
.partners{position:absolute;left:50px;top:614px;display:flex;gap:26px;font:700 11px "Lato",sans-serif;color:#4a4a4a}
.divider{position:absolute;left:412px;top:72px;width:1px;height:560px;background:var(--line)}
.customers{position:absolute;left:423px;top:72px;width:88px}
.customers h3{font:400 12px/1.2 "Lato",sans-serif;color:#333;text-transform:uppercase;margin-bottom:10px}
.customer{height:40px;margin-bottom:8px;border:1px solid #cfcfcf;border-radius:3px;display:flex;align-items:center;justify-content:center;text-align:center;font:700 8.5px/1.1 "Lato",sans-serif;color:#4a4a4a;padding:2px}
</style>
</head>
<body>

<div class="page-label" style="left:252px">Page 3</div>
<div class="page-label" style="left:855px">Page 4</div>

<section class="page page--products">
  <header class="masthead">
    <svg width="550" height="62" viewBox="0 0 550 62"><path d="M0 0H550V44C470 44 300 40 200 46C140 50 90 58 0 56Z" fill="var(--green)"/></svg>
    <div class="masthead__art" role="img" aria-label="Loudspeakers and music notes decoration"></div>
    <div class="brand"><span class="brand__mark"></span><span class="brand__name">BrightWave<br>Audio Services</span></div>
  </header>

  <h1 class="title">PRODUCTS<small>PROVEN SOLUTIONS FOR OPTIMAL VALUE.</small></h1>

  <div class="block" style="left:50px;top:126px;width:263px">
    <h2 class="section-head">SOUNDLOOM</h2>
    <div class="kicker">SOUNDLOOM – SOUND SOLUTIONS FOR BUSINESS</div>
    <p>Only SOUNDLOOM offers premium sound with customized messaging for your business in an all-in-one, high quality solution.</p>
    <ul class="bullets">
      <li>Over 50 quality channels of commercial-free music</li>
      <li>Custom channel creation</li>
      <li>Customized messaging creation</li>
      <li>Real-time control over music and messaging</li>
      <li>Starting at $27.95/month</li>
    </ul>
  </div>

  <div class="block" style="left:50px;top:298px;width:263px">
    <h2 class="section-head">MESSAGING</h2>
    <div class="kicker">SPECIALIZED DELIVERY. CUSTOMIZED MESSAGING.</div>
    <p>Build the image of your business with professionally recorded, customized messages to support your sales efforts and enhance already in-place marketing strategies.</p>
    <ul class="bullets">
      <li>Professional Script Writing</li>
      <li>Production and Recording by Industry Leaders</li>
      <li>Expert Installation and Support Services</li>
      <li>Scalable to Meet Business Needs of Any Size</li>
    </ul>
  </div>

  <div class="block" style="left:50px;top:452px;width:263px">
    <h3 class="minor-head">MESSAGE DELIVERY</h3>
    <p>Using our proprietary software/online portal, you’re able to schedule your messages to run at desired intervals and time periods, including yearly, quarterly, monthly, weekly, daily, by time of day, by holiday, by market window, and more.</p>
    <p>You can even choose to lock your messages; an important feature for our corporate and franchise clients who need to guarantee certain messages run within their local stores.</p>
  </div>

  <div class="block" style="left:50px;top:565px;width:263px">
    <h3 class="minor-head">MESSAGE MANAGEMENT</h3>
    <p>Messages are uploaded via our online portal and into accounts where they are scheduled in real-time to devices on-location. You can manage and schedule your messages on a single player or across a group of players. Group player management allows you to manage messages across a region, state, city, or group of players selected.</p>
  </div>

  <div class="block" style="left:380px;top:126px;width:131px">
    <h2 class="section-head">ORBIT RADIO</h2>
    <div class="kicker" style="text-transform:none">OrbitFM FOR BUSINESS.<br>OrbitFM FOR YOU.</div>
    <p>OrbitFM Radio Business Music Service is a great, low-cost alternative to other music providers. Enjoy a variety of audio options, all free of commercial interruption for one low monthly payment, with no contract required.</p>
    <ul class="bullets bullets--caps">
      <li>Low monthly fees</li>
      <li>No commercials</li>
      <li>Wide variety of programming options</li>
      <li>No long-term contracts</li>
      <li>Multiple billing options</li>
      <li>Easy installation</li>
      <li>Customized channel blocking available</li>
    </ul>
  </div>

  <div class="illustration" style="left:345px;top:398px;width:168px;height:262px" role="img" aria-label="Illustration of photos streaming into a desktop screen showing the company name"></div>

  <footer class="footer">
    <svg width="550" height="70" viewBox="0 0 550 70"><path d="M0 4H150C168 4 172 16 190 16H550V70H0Z" fill="var(--footer)"/></svg>
    <div class="footer__call">CALL TODAY<span>800.555.0147</span></div>
    <div class="footer__web">BRIGHTWAVEAUDIOSERVICES.com</div>
  </footer>
</section>

<section class="page page--advantage">
  <header class="masthead">
    <svg width="550" height="62" viewBox="0 0 550 62"><path d="M0 0H550V44C470 44 300 40 200 46C140 50 90 58 0 56Z" fill="var(--green)"/></svg>
    <div class="masthead__art" role="img" aria-label="Loudspeakers and music notes decoration"></div>
    <div class="brand"><span class="brand__mark"></span><span class="brand__name">BrightWave<br>Audio Services</span></div>
  </header>

  <div class="block" style="left:50px;top:75px;width:325px">
    <h2 class="section-head" style="font-size:15.5px">EXPERIENCE THE BRIGHTWAVE ADVANTAGE.</h2>
    <p>BRIGHTWAVE AUDIO SERVICES™ is committed to delivering businesses the marketing advantage of providing licensed, in-store music and messaging, customized for their consumers. Using real-time management of media players at national, regional and local store levels, BRIGHTWAVE AUDIO SERVICES™ aims to carry out a strategically developed mission, backed by a vision designed to specifically meet client needs and the needs of their consumers.</p>
  </div>

  <div class="block" style="left:50px;top:180px;width:325px">
    <h3 class="minor-head minor-head--muted">OUR MISSION</h3>
    <p class="lead">To provide quality in-store music and messaging services empowered by hard work, ingenuity and integrity.</p>
    <p style="width:230px;text-align:left">To realize this mission, we have developed an industry leading solution for the delivery and management of digital assets that combines the power of the Internet with the flexibility of software.</p>
  </div>

  <div class="block" style="left:50px;top:273px;width:230px">
    <h3 class="minor-head minor-head--muted">OUR VISION</h3>
    <p style="text-align:left">Producing innovative and affordable business audio solutions, utilizing the latest technology and the brightest minds.</p>
  </div>

  <div class="puzzle" style="left:282px;top:236px;width:112px;height:100px" role="img" aria-label="Crossword tiles spelling mission and vision"></div>

  <div class="block" style="left:50px;top:330px;width:325px">
    <h2 class="section-head">WHY BRIGHTWAVE?</h2>
    <div class="kicker">TAKE YOUR BUSINESS TO THE NEXT LEVEL.</div>
    <p>As the leading provider of audio, video and messaging services for businesses throughout the US, we offer quality products and services coupled with premium customer support to deliver a unique and stress-free streaming music solution for our customers.</p>
  </div>

  <div class="block quote" style="left:50px;top:424px;width:325px">Experience the optimal advantage<br>with BRIGHTWAVE AUDIO SERVICES™</div>

  <div class="block" style="left:50px;top:488px;width:325px">
    <h2 class="section-head">TECHNOLOGY</h2>
    <div class="kicker">GET TOMORROW’S TECHNOLOGY, TODAY.</div>
    <p>BRIGHTWAVE AUDIO SERVICES™ employs our own propriety software solutions, both built and hosted on a best-in-class, Class-A hybrid foundation. Our application and database servers live within the Stackhouse Enterprise Cloud Network, whereas our Digital Asset Delivery is hosted within the Nimbus Intelligent Platform with all data synced in real-time via the Nimbus API. By utilizing the Stackhouse Cloud Network and the Nimbus Intelligent Platform we are able to ramp up distribution and support for an unlimited number of media devices on a global scale.</p>
  </div>

  <div class="partners"><span>Nimbus</span><span>Stackhouse</span><span>Northsoft</span><span>Flowcast</span></div>

  <div class="divider"></div>
  <aside class="customers">
    <h3>Some of our customers</h3>
    <div class="customer">Golden Grill</div>
    <div class="customer">Frosty Cup</div>
    <div class="customer">Corner Stop</div>
    <div class="customer">Royal Patty</div>
    <div class="customer">Valley Medical Center</div>
    <div class="customer">CareQuick</div>
    <div class="customer">Oldtown Burgers</div>
    <div class="customer">Sunny Skillet</div>
    <div class="customer">Chef Supply</div>
    <div class="customer">Valley Health System</div>
    <div class="customer">Ridgeline</div>
  </aside>

  <footer class="footer">
    <svg width="550" height="70" viewBox="0 0 550 70"><path d="M0 4H150C168 4 172 16 190 16H550V70H0Z" fill="var(--footer)"/></svg>
    <div class="footer__call">CALL TODAY<span>800.555.0147</span></div>
    <div class="footer__web">BRIGHTWAVEAUDIOSERVICES.com</div>
  </footer>
</section>

</body>
</html>
```